New Webpage for High Class Expert Witness Services Company

We are looking for a minimalist design for a webpage that just has our logo and an entry form offer to connect with one of our Liaisons.
The entry form should just ask for Name, Email, Contact Info and Description of Project.

Company Name is: The Marlow Crest Advisory Services

Number of Pages Required

1 page

```html
<!DOCTYPE html>
<html lang="en">
<head>
<meta charset="utf-8">
<title>The Marlow Crest Advisory Services — Speak With a Liaison</title>
<link href="https://fonts.googleapis.com/css2?family=Cinzel:wght@500;600&family=Poppins:wght@400;500;700&display=swap" rel="stylesheet">
<style>
  :root {
    --copper: #b07149;
    --ink-dark: #2b2b2d;
    --ink-deep: #232325;
    --footer: #1b1b1c;
    --white: #ffffff;
    --field-text: #2a2a2a;
    --divider: #d9d9d9;
  }
  * { box-sizing: border-box; margin: 0; padding: 0; }
  html, body { width: 1057px; height: 1200px; overflow: hidden; }
  body {
    position: relative;
    font-family: "Poppins", sans-serif;
    color: var(--white);
    background: var(--ink-dark);
  }
  .hero {
    position: absolute; left: 0; top: 0; width: 1057px; height: 453px;
    background:
      radial-gradient(ellipse at 50% 30%, #b9b9b9 0%, #8d8d8d 45%, #5e5e5e 100%),
      #777;
  }
  .hero::after {
    content: ""; position: absolute; inset: 0;
    background: linear-gradient(90deg, rgba(230,230,230,.35) 0%, rgba(0,0,0,0) 35%, rgba(0,0,0,0) 70%, rgba(20,20,20,.55) 100%);
  }
  .brand {
    position: absolute; left: 0; right: 0; top: 196px;
    display: flex; justify-content: center; align-items: center; gap: 14px;
    z-index: 1;
  }
  .brand-mark { width: 14px; height: 14px; background: var(--white); }
  .brand-name {
    font-family: "Cinzel", serif; font-weight: 500;
    font-size: 36px; letter-spacing: 1px; color: var(--white);
  }
  .contact {
    position: absolute; left: 0; top: 453px; width: 1057px; height: 690px;
    background: linear-gradient(90deg, #3a3a3c 0%, #2e2e30 55%, var(--ink-deep) 100%);
    text-align: center;
  }
  .contact-title {
    position: absolute; left: 0; right: 0; top: 148px;
    font-family: "Cinzel", serif; font-weight: 600;
    font-size: 45px; line-height: 47px; letter-spacing: .5px;
  }
  .title-rule {
    position: absolute; left: 490px; top: 246px; width: 76px; height: 2px;
    background: var(--copper);
  }
  .lead {
    position: absolute; left: 0; right: 0; top: 276px;
    font-size: 16px; line-height: 25px; font-weight: 500;
  }
  .lead + .lead { top: 315px; }
  .field {
    position: absolute; background: var(--white); border-radius: 22px;
    display: flex; align-items: center; color: var(--field-text);
    font-size: 14px; font-weight: 500; text-align: left;
  }
  .field-icon {
    width: 48px; height: 32px; display: flex; align-items: center; justify-content: center;
    border-right: 1px solid var(--divider); margin-right: 13px;
  }
  .field-icon svg { width: 13px; height: 13px; fill: var(--copper); }
  .field--name { left: 160px; top: 394px; width: 360px; height: 44px; }
  .field--email { left: 160px; top: 452px; width: 360px; height: 44px; }
  .field--phone { left: 160px; top: 510px; width: 360px; height: 44px; }
  .field--project { left: 534px; top: 394px; width: 363px; height: 159px; border-radius: 18px; align-items: flex-start; padding-top: 8px; }
  .field--project .field-icon { height: 36px; }
  .field--project .field-label { margin-top: 9px; }
  .submit {
    position: absolute; left: 417px; top: 573px; width: 224px; height: 45px;
    border-radius: 23px; background: var(--copper); color: var(--white);
    font-weight: 700; font-size: 15px; display: flex; align-items: center; justify-content: center;
  }
  .footer {
    position: absolute; left: 0; top: 1143px; width: 1057px; height: 57px;
    background: var(--footer); display: flex; align-items: center; justify-content: center;
    font-size: 12px;
  }
</style>
</head>
<body>
  <header class="hero" role="img" aria-label="Black and white photograph of a doctor in a white coat shaking hands with a businessman in a suit, hospital corridor behind">
    <div class="brand">
      <span class="brand-mark"></span>
      <span class="brand-name">Marlow Crest Advisory Services</span>
    </div>
  </header>

  <main class="contact">
    <h1 class="contact-title">SPEAK WITH A DEFENSE<br>LIAISON TODAY</h1>
    <div class="title-rule"></div>
    <p class="lead">Direct access to experienced professionals for your mission-critical projects.</p>
    <p class="lead">Share a few details about your project, and a member of our team will reach out to discuss<br>how we can support your objectives.</p>

    <div class="field field--name">
      <span class="field-icon"><svg viewBox="0 0 16 16"><circle cx="8" cy="4.5" r="3.5"/><path d="M1.5 16c0-4.5 3-7 6.5-7s6.5 2.5 6.5 7z"/></svg></span>
      <span class="field-label">Your Name</span>
    </div>
    <div class="field field--email">
      <span class="field-icon"><svg viewBox="0 0 16 16"><path d="M3.6 1l2.6 3.2-1.6 1.9c.9 2 2.4 3.6 4.4 4.5l1.9-1.6 3.1 2.6-1.4 2.9C6.4 14.2 1.6 9.4 1.1 3z"/></svg></span>
      <span class="field-label">Email</span>
    </div>
    <div class="field field--phone">
      <span class="field-icon"><svg viewBox="0 0 16 16"><path d="M1 3h14v1.2L8 8.6 1 4.2z"/><path d="M1 5.8l7 4.4 7-4.4V13H1z"/></svg></span>
      <span class="field-label">Phone</span>
    </div>
    <div class="field field--project">
      <span class="field-icon"><svg viewBox="0 0 16 16"><ellipse cx="6.5" cy="6" rx="6" ry="4.2"/><path d="M2.5 9l-1 3 3.5-2z"/><path d="M13.5 6.5c1.2.8 2 1.9 2 3.1 0 1-.5 1.9-1.4 2.6l.8 2.3-2.8-1.5c-.6.2-1.3.3-2 .3-1.7 0-3.2-.6-4.1-1.5 4.3-.2 7.5-2.3 7.5-5.3z"/></svg></span>
      <span class="field-label">Project Description</span>
    </div>

    <div class="submit">SUBMIT REQUEST</div>
  </main>

  <footer class="footer">Copyright © 2026 The Marlow Crest Advisory Services&nbsp; | &nbsp;All Rights Reserved</footer>
</body>
</html>
```